Flat Belly Design Graphics for Social

I want to create 9 social media graphics (new Instagram size 4:5 (1080 x 1350 pixels) focusing on our Flat Belly Graphics, using the pics attached. Use the attached pics, NO RANDOM STOCK PHOTOGRAPHY. For the color scheme of the graphics, the color palette is attached. YOU MUST POST ALL 9 GRAPHICS IN ONE ENTRY.
Using the 3 titles below, create one set of graphics. 1) with all text, then for the others, use the pictures as detailed below in IMPORTANT:
1. 21-Night Lean Middle Reboot Beyond 50
2. The 20-Second Trim-Core Menu Guide
3. Starlet Tricks to a Slender Midline Beyond 50 - Zero Scalpel Needed
IMPORTANT:
Only use RK Pic 1 and RK Pic 2 with the title, 21-Night Lean Middle Reboot Beyond 50
Only use meal plan1 and meal plan2 pics with the title, 20-Second Trim-Core Menu Guide
Only use starlet tricks 1 and starlet tricks 2 pics with the title, Starlet Tricks to a Slender Midline Beyond 50 - Zero Scalpel Needed
women over 40

```html
<!DOCTYPE html>
<html lang="en">
<head>
<meta charset="utf-8">
<title>Lean Middle Social Set</title>
<link href="https://fonts.googleapis.com/css2?family=League+Spartan:wght@500;700;800&family=Allura&display=swap" rel="stylesheet">
<style>
  :root{
    --ink:#2f4d48;
    --rose:#e3a3b8;
    --rose-deep:#d98aa5;
    --blush:#fbe8ec;
    --blush-soft:#fdf3f5;
    --stage:#eef2ef;
    --band:rgba(47,77,72,.85);
  }
  *{margin:0;padding:0;box-sizing:border-box}
  html,body{width:960px;height:1200px;overflow:hidden}
  body{
    background:radial-gradient(circle at 50% 45%,#f8faf8 0%,var(--stage) 100%);
    font-family:"League Spartan",Arial,sans-serif;
    color:var(--ink);
    position:relative;
  }
  .card{
    position:absolute;width:258px;height:322px;overflow:hidden;
    background:radial-gradient(circle at 60% 45%,#fff7f8 0%,var(--blush) 75%);
    box-shadow:0 10px 12px -6px rgba(0,0,0,.28);
  }
  .c1{left:58px;top:62px}.c2{left:351px;top:62px}.c3{left:644px;top:62px}
  .c4{left:58px;top:433px}.c5{left:351px;top:433px}.c6{left:644px;top:433px}
  .c7{left:58px;top:800px}.c8{left:351px;top:800px}.c9{left:644px;top:800px}

  .block{position:absolute;left:0;right:0;text-align:center}
  .kicker{font-weight:500;font-size:19px;letter-spacing:-.5px}
  .kicker .the{font-family:"Allura",cursive;color:var(--rose-deep);font-size:24px;margin-right:2px}
  .headline{font-weight:700;text-transform:uppercase;line-height:.86;letter-spacing:-1.5px}
  .headline small{font-size:.5em;letter-spacing:-.5px}
  .script{font-family:"Allura",cursive;color:var(--rose-deep);line-height:1;position:absolute;white-space:nowrap}
  .script svg{width:10px;height:10px;vertical-align:top;margin-right:2px}
  .stamp{
    position:absolute;border:1.5px solid var(--rose);color:var(--ink);
    font-weight:700;text-transform:uppercase;text-align:center;line-height:.95;
    transform:rotate(-6deg);letter-spacing:-.3px;
  }
  .photo{position:absolute}
  .band{position:absolute;left:0;right:0;background:var(--band);color:#fff;text-align:center;font-weight:700;text-transform:uppercase;letter-spacing:-1px}
  .strip{position:absolute;left:0;right:0;bottom:0;height:8px;background:var(--rose)}
</style>
</head>
<body>
<svg width="0" height="0" style="position:absolute">
  <defs>
    <symbol id="spark" viewBox="0 0 10 10"><path d="M5 0v10M0 5h10M1.5 1.5l7 7M8.5 1.5l-7 7" stroke="#d98aa5" stroke-width="1.2"/></symbol>
  </defs>
</svg>

<!-- Reboot: text only -->
<section class="card c1">
  <div class="block kicker" style="top:40px">21-Night</div>
  <div class="block headline" style="top:70px;font-size:46px">Lean<br>Middle<br>Reboot</div>
  <div class="script" style="left:66px;top:218px;font-size:44px;transform:rotate(-14deg)"><svg><use href="#spark"/></svg>Beyond 50</div>
</section>

<!-- Reboot: portrait centered -->
<section class="card c2">
  <div class="block kicker" style="top:22px">21-Night</div>
  <div class="block headline" style="top:44px;font-size:34px">Lean Middle<br>Reboot</div>
  <div class="script" style="left:132px;top:104px;font-size:26px;transform:rotate(-12deg)">Beyond 50</div>
  <div class="photo" role="img" aria-label="Smiling woman in a white cropped sweater and black trousers pointing at her waist" style="left:58px;top:140px;width:142px;height:182px;background:radial-gradient(ellipse at 50% 45%,#f3ecea 0%,#d9cfcc 45%,#e8b9c6 80%,rgba(251,232,236,0) 100%)"></div>
</section>

<!-- Reboot: portrait in kitchen -->
<section class="card c3">
  <div class="block kicker" style="top:14px">21-Night</div>
  <div class="block headline" style="top:36px;font-size:33px">Lean Middle<br>Reboot</div>
  <div class="script" style="left:132px;top:94px;font-size:25px;transform:rotate(-12deg)">Beyond 50</div>
  <div class="photo" role="img" aria-label="Smiling woman in a white cropped sweater standing in a wood-panelled kitchen" style="left:0;top:134px;width:258px;height:188px;background:linear-gradient(180deg,#5a3426 0%,#7a4c37 45%,#b48a6e 62%,#4a2a1f 100%)"></div>
</section>

<!-- Menu guide: text only -->
<section class="card c4">
  <div class="block kicker" style="top:62px"><span class="the">The</span>20-Second</div>
  <div class="block headline" style="top:100px;font-size:56px">Trim-<br>Core</div>
  <div class="block headline" style="top:212px;font-size:34px">Menu Guide</div>
</section>

<!-- Menu guide: food spread -->
<section class="card c5">
  <div class="block kicker" style="top:24px"><span class="the">The</span>20-Second</div>
  <div class="block headline" style="top:54px;font-size:36px">Trim-Core<br>Menu Guide</div>
  <div class="photo" role="img" aria-label="Overhead spread of chicken, berries, potatoes, asparagus and grains around a meal planner on a wooden table" style="left:0;top:138px;width:258px;height:160px;background:linear-gradient(135deg,#e9c9b8 0%,#6b4a36 35%,#c43a3a 55%,#5d3d2b 75%,#9aa74a 100%)"></div>
  <div class="band" style="top:292px;height:22px"></div>
  <div class="strip"></div>
</section>

<!-- Menu guide: food with banner -->
<section class="card c6">
  <div class="block kicker" style="top:24px"><span class="the">The</span>20-Second</div>
  <div class="block headline" style="top:48px;font-size:44px">Trim-<br>Core</div>
  <div class="photo" role="img" aria-label="Salmon, eggs, avocado, vegetables and chicken around a meal planner on dark wood" style="left:0;top:164px;width:258px;height:150px;background:linear-gradient(135deg,#e98a6a 0%,#5b3c2a 30%,#3f2a20 60%,#7c9a45 85%,#c53b3b 100%)"></div>
  <div class="band" style="top:268px;height:44px;font-size:34px;line-height:48px">Menu Guide</div>
  <div class="strip"></div>
</section>

<!-- Starlet tricks: text only -->
<section class="card c7">
  <div class="block headline" style="top:52px;font-size:36px;line-height:.82">Starlet<br>Tricks <small>to</small><br><span style="font-size:27px">A Slender Midline</span></div>
  <div class="script" style="left:82px;top:160px;font-size:40px;transform:rotate(-14deg)"><svg><use href="#spark"/></svg>Beyond 50</div>
  <div class="stamp" style="left:62px;top:246px;width:138px;font-size:16px;padding:4px 2px">Zero Scalpel<br>Needed</div>
</section>

<!-- Starlet tricks: photo top -->
<section class="card c8">
  <div class="photo" role="img" aria-label="Two women, one whispering a secret to the other who looks surprised" style="left:0;top:0;width:258px;height:140px;background:linear-gradient(120deg,#3b2a22 0%,#8a5c44 35%,#e8d2c4 60%,#c79a86 100%)"></div>
  <div class="block headline" style="top:150px;font-size:36px;line-height:.82">Starlet<br>Tricks <small>to</small><br><span style="font-size:27px">A Slender Midline</span></div>
  <div class="script" style="left:22px;top:266px;font-size:30px;transform:rotate(-12deg)"><svg><use href="#spark"/></svg>Beyond 50</div>
  <div class="stamp" style="left:174px;top:262px;width:72px;font-size:10px;padding:3px 1px">Zero Scalpel<br>Needed</div>
</section>

<!-- Starlet tricks: photo bottom -->
<section class="card c9">
  <div class="block headline" style="top:32px;font-size:34px;line-height:.82">Starlet<br>Tricks <small>to</small><br><span style="font-size:25px">A Slender Midline</span></div>
  <div class="script" style="left:96px;top:122px;font-size:32px;transform:rotate(-14deg)"><svg><use href="#spark"/></svg>Beyond 50</div>
  <div class="photo" role="img" aria-label="Two women in casual tops and jeans, one whispering to the other who looks delighted" style="left:66px;top:178px;width:126px;height:144px;background:radial-gradient(ellipse at 50% 50%,#c99a82 0%,#9fb4c9 50%,rgba(251,232,236,0) 78%)"></div>
  <div class="stamp" style="left:178px;top:266px;width:70px;font-size:10px;padding:3px 1px">Zero Scalpel<br>Needed</div>
</section>
</body>
</html>
```